Business and Success Coaching Business Card

Need a business card for my coaching business. I coach small businesses, career professionals and, individuals wanting to unlock their human potential and achieve excellence. At the heart of our methodology is the Shaping Purposeful Action Routines Knowingly (SPARK) approach to formulate empowerment, create principles for success and setting achievable outcomes. I would like something that incorporates our new logo, something clean and sharp with a solid darker, but complementary background, color on the card front. The back should be white where there will be room for three questions

Target Market(s)

People looking to advance and improve themselves through a success coach

Industry/Entity Type

Life Coaching

Contact Information for Business Card

Contact information on card.
Business name on front of card
Questions on back

Font styles to use
Other font styles liked:
• Century Gothic or other Serif style fonts that look similar to Century Gothic

Colors

Designer to choose colors to be used in the design.

Requirements
Must have
• Logo on front of card
• Business name - The Steady Forge
• Contact name - Ted Harlow
• Address - Box 4619, Littleton, CO 80127-4619
• Phone number - 303-555-0147
• Email address - harlow.ted@thesteadyforge.example
• Certifications - CSC, CCHt, PTT, PNLP
• Back of card
• Three questions on the back of the card:
• If you were at your best, what would you do right now?
• What is the decision you have been avoiding?
• What's one action you could take in the next 10 minutes?
Nice to have
• I would like to see a solid color on the front of the card that compliments the logo.
• Back should be white, or could be contrasting, but need to have the three questions.

```html
<!DOCTYPE html>
<html lang="en">
<head>
<meta charset="utf-8">
<title>The Steady Forge — Business Card</title>
<link href="https://fonts.googleapis.com/css2?family=Questrial&family=Montserrat:wght@600&display=swap" rel="stylesheet">
<style>
  :root {
    --page: #2a2d33;
    --navy: #1f366f;
    --white: #ffffff;
    --ink-navy: #1f3473;
    --ink-gray: #5a5d66;
    --rule: #8a93b5;
    --map-tint: #f1f2f4;
  }
  * { box-sizing: border-box; margin: 0; padding: 0; }
  html, body { width: 1200px; height: 1000px; overflow: hidden; }
  body {
    background: var(--page);
    font-family: "Questrial", "Century Gothic", sans-serif;
    position: relative;
  }
  .card {
    position: absolute;
    width: 760px;
    height: 434px;
    box-shadow: 0 10px 30px rgba(0,0,0,.45);
  }
  /* Back of card */
  .card-back { left: 360px; top: 36px; background: var(--white); }
  .card-back .map-area {
    position: absolute;
    left: 190px; top: 60px;
    width: 460px; height: 300px;
    background: radial-gradient(ellipse at center, var(--map-tint) 55%, rgba(241,242,244,0) 75%);
  }
  .questions {
    position: absolute;
    left: 0; right: 0; top: 150px;
    display: flex; flex-direction: column; align-items: center;
  }
  .question {
    font-size: 23px;
    letter-spacing: .5px;
    color: var(--ink-navy);
    padding: 0 20px 8px;
    width: 620px;
    text-align: center;
  }
  .question + .question { margin-top: 18px; }
  .question:not(:last-child) { border-bottom: 1px solid var(--rule); }
  .question.muted { color: var(--ink-gray); }

  /* Front of card */
  .card-front { left: 90px; top: 510px; background: var(--navy); color: var(--white); }
  .person { position: absolute; left: 52px; top: 46px; }
  .person-name {
    font-family: "Montserrat", "Century Gothic", sans-serif;
    font-weight: 600;
    font-size: 38px;
    letter-spacing: .5px;
  }
  .person-title { font-size: 22px; margin-top: 2px; }
  .details { position: absolute; left: 52px; top: 160px; font-size: 21px; line-height: 1.3; }
  .details .certs { margin-bottom: 8px; }
  .contacts { position: absolute; left: 52px; top: 285px; list-style: none; font-size: 21px; }
  .contacts li { display: flex; align-items: center; gap: 12px; line-height: 1.55; }
  .contacts svg { width: 18px; height: 18px; flex: none; }
  .brand {
    position: absolute;
    right: 56px; top: 176px;
    font-family: "Montserrat", "Century Gothic", sans-serif;
    font-weight: 600;
    font-size: 34px;
    color: var(--white);
  }
</style>
</head>
<body>

<section class="card card-back" aria-label="Card back">
  <div class="map-area" role="img" aria-label="Faint world map background"></div>
  <div class="questions">
    <p class="question">What is the decision you have been avoiding?</p>
    <p class="question muted">If you were at your best, what would you do right now?</p>
    <p class="question">What's one action you could take in the next 10 minutes?</p>
  </div>
</section>

<section class="card card-front" aria-label="Card front">
  <div class="person">
    <h1 class="person-name">Ted Harlow</h1>
    <p class="person-title">Manager</p>
  </div>
  <div class="details">
    <p class="certs">CSC, CCHt, PTT, PNLP</p>
    <p>Box 4619,<br>Littleton, CO 80127-4619</p>
  </div>
  <ul class="contacts">
    <li>
      <svg viewBox="0 0 24 24" aria-hidden="true"><path fill="#fff" d="M6.6 10.8c1.4 2.8 3.8 5.1 6.6 6.6l2.2-2.2c.3-.3.7-.4 1-.2 1.1.4 2.3.6 3.6.6.6 0 1 .4 1 1V20c0 .6-.4 1-1 1C10.6 21 3 13.4 3 4c0-.6.4-1 1-1h3.5c.6 0 1 .4 1 1 0 1.3.2 2.5.6 3.6.1.3 0 .7-.2 1z"/></svg>
      303-555-0147
    </li>
    <li>
      <svg viewBox="0 0 24 24" aria-hidden="true"><rect x="2.5" y="5" width="19" height="14" fill="none" stroke="#fff" stroke-width="2"/><path d="M3 6l9 7 9-7" fill="none" stroke="#fff" stroke-width="2"/></svg>
      harlow.ted@thesteadyforge.example
    </li>
    <li>
      <svg viewBox="0 0 24 24" aria-hidden="true"><circle cx="12" cy="12" r="9" fill="none" stroke="#fff" stroke-width="2"/><path d="M3 12h18M12 3c3 3 3 15 0 18M12 3c-3 3-3 15 0 18" fill="none" stroke="#fff" stroke-width="1.5"/></svg>
      www.thesteadyforge.example
    </li>
  </ul>
  <p class="brand">The Steady Forge</p>
</section>

</body>
</html>
```